New business card, letter head, email signature and Portfolio for our Security company.

We are an Elite security company that provides a top quality manpower services to protect high rise buildings, retail and all type of properties and would like a new business card/logo look.

- We would like the spot UV design.
- Matt black (double sided).
- We would like to incorporate a royal blue colour (feel free to experiment with it).
- Feel free to try different lengths with the card to make it stand out more than a normal business card.
- We would like the logo to be an eagle eye in the background (shines when card is tilted slightly in the background, either on the front, back or both sides of the card). Image attached as an example of eye shape (colour to be either black or royal blue).
- MAVRIN OAK GUARD PATROLS PTY. LTD. and MOGP to be placed on one side of the card and on the other side of the card to have;

- Name in slightly bigger font than the position (directly on the bottom on the name).
- Mobile number
- Email address
- Website email address
- PO BOX address

Can we please have the files in a format that we can edit.

Reason: I need to consult my business partner with the designs so far and will make a decision from there.

Target Market(s)

Security Industry

Industry/Entity Type

Business

Contact Information for Business Card

- Mobile number
- Email address
- Website email address
- PO BOX address

Logo Text

MOGP and underneath the MOGP please add MAVRIN OAK GUARD PATROLS PTY. LTD.

Font styles to use
Other font styles liked:
• bold type font

Colors
0255a3
000000

Requirements
Must have
• We are an Elite security company that provides a top quality manpower services to protect high rise buildings, retail and all type of properties and would like a new business card/logo look.
• - We would like the spot UV design.
• - Matt black (double sided).
• - We would like to incorporate a royal blue colour (feel free to experiment with it).
• - Feel free to try different lengths with the card to make it stand out more than a normal business card.
• - We would like the logo to be an eagle eye in the background (shines when card is tilted slightly in the background, either on the front, back or both sides of the card). Image attached as an example of eye shape (colour to be either black or royal blue).
• - MAVRIN OAK GUARD PATROLS PTY. LTD. and MOGP to be placed on one side of the card and on the other side of the card to have;
• - Name in slightly bigger font than the position (directly on the bottom on the name).
• - Mobile number
• - Email address
• - Website email address
• - PO BOX address
• Can we please have the files in a format that we can edit.
Nice to have
• Feel free to try different lengths with the card to make it stand out more than a normal business card.
• Please find "URBAN JUNGLE" font attached and incorporate MOGP into the same style with building's inside the MOGP bold front also add MAVRIN into the bottom part of the S and follow on E - Elite on the bottom S - SECURITY on the bottom S - SERVICES on the bottom of each letter.
• other than that, I'll be happy with a bold modern font for the MOGP and MAVRIN OAK GUARD PATROLS in a bold and thinner font underneath.

```html
<!DOCTYPE html>
<html lang="en">
<head>
<meta charset="utf-8">
<title>MOGP Business Card</title>
<link rel="stylesheet" href="https://fonts.googleapis.com/css2?family=Open+Sans:wght@400;600;700;800&display=swap">
<style>
  :root {
    --backdrop: #2e2926;
    --card-black: #141414;
    --card-edge: #0b0b0b;
    --ink-white: #ffffff;
    --ink-silver: #8f8f8f;
    --royal-blue: #0255a3;
    --divider: #6a6a6a;
  }
  * { margin: 0; padding: 0; box-sizing: border-box; }
  html, body {
    width: 1200px; height: 780px; overflow: hidden;
    background: var(--backdrop);
    font-family: "Open Sans", Verdana, sans-serif;
  }
  .canvas {
    position: relative; width: 1200px; height: 780px;
    display: flex; align-items: center; justify-content: center; gap: 50px;
  }
  .card {
    position: relative; width: 540px; height: 310px;
    background: var(--card-black);
    border: 1px solid var(--card-edge);
    box-shadow: 0 12px 30px rgba(0,0,0,0.45);
  }

  /* Front: brand wordmark */
  .card-front { display: flex; flex-direction: column; align-items: center; justify-content: center; }
  .card-front .brand-mark {
    font-weight: 800; font-size: 84px; letter-spacing: 10px;
    color: var(--ink-silver); line-height: 1;
  }
  .card-front .brand-line {
    margin-top: 10px; font-weight: 800; font-size: 17px; letter-spacing: 1px;
    color: var(--ink-silver);
  }

  /* Back: brand + contact */
  .card-back { display: flex; align-items: center; }
  .back-brand {
    width: 262px; display: flex; flex-direction: column; align-items: center; justify-content: center;
    padding-left: 14px;
  }
  .back-brand .brand-mark {
    font-weight: 800; font-size: 62px; letter-spacing: 6px; color: var(--ink-white); line-height: 1;
  }
  .back-brand .brand-line {
    margin-top: 8px; font-weight: 800; font-size: 12.5px; letter-spacing: 0.5px; color: var(--ink-white);
  }
  .back-divider { width: 1px; height: 170px; background: var(--divider); margin: 0 22px 0 14px; }
  .contact { color: var(--ink-white); }
  .contact .person-name { font-weight: 700; font-size: 22px; line-height: 1.1; }
  .contact .person-role { font-size: 13px; color: var(--royal-blue); margin-bottom: 14px; }
  .contact-row { display: flex; align-items: center; gap: 8px; font-size: 14px; font-weight: 600; line-height: 1.55; }
  .contact-icon { width: 14px; height: 14px; flex: none; }
  .contact .postal { margin-top: 8px; font-size: 14px; font-weight: 600; line-height: 1.4; }
</style>
</head>
<body>
<main class="canvas">
  <section class="card card-front" aria-label="Card front">
    <div class="brand-mark">MOGP</div>
    <div class="brand-line">MAVRIN OAK GUARD PATROLS</div>
  </section>

  <section class="card card-back" aria-label="Card back">
    <div class="back-brand">
      <div class="brand-mark">MOGP</div>
      <div class="brand-line">MAVRIN OAK GUARD PATROLS</div>
    </div>
    <div class="back-divider"></div>
    <div class="contact">
      <div class="person-name">Employee Name</div>
      <div class="person-role">Manager</div>
      <div class="contact-row">
        <svg class="contact-icon" viewBox="0 0 14 14" aria-hidden="true">
          <rect width="14" height="14" fill="#0255a3"/>
          <rect x="4.5" y="2.5" width="5" height="9" rx="1" fill="none" stroke="#fff" stroke-width="1.2"/>
          <circle cx="7" cy="9.8" r="0.7" fill="#fff"/>
        </svg>
        <span>0123 456 789</span>
      </div>
      <div class="contact-row">
        <svg class="contact-icon" viewBox="0 0 14 14" aria-hidden="true">
          <rect width="14" height="14" fill="#0255a3"/>
          <rect x="2.5" y="4" width="9" height="6.5" fill="none" stroke="#fff" stroke-width="1.1"/>
          <path d="M2.5 4 L7 8 L11.5 4" fill="none" stroke="#fff" stroke-width="1.1"/>
        </svg>
        <span>hello@mogpmail.net.nz</span>
      </div>
      <div class="contact-row">
        <svg class="contact-icon" viewBox="0 0 14 14" aria-hidden="true">
          <rect width="14" height="14" fill="#0255a3"/>
          <circle cx="7" cy="7" r="4.3" fill="none" stroke="#fff" stroke-width="1"/>
          <ellipse cx="7" cy="7" rx="1.8" ry="4.3" fill="none" stroke="#fff" stroke-width="0.9"/>
          <path d="M2.7 7 H11.3" stroke="#fff" stroke-width="0.9"/>
        </svg>
        <span>www.mogpguard.co.nz</span>
      </div>
      <div class="postal">P.O. Box 000, Fern Row<br>Harlow Bay, New Zealand</div>
    </div>
  </section>
</main>
</body>
</html>
```